Modern corporate energy/fuel business need business card design

Business card required for company founder. Korvan Fuel Works is a Australian based modern energy/fuel provider. We offer specialised solutions to businesses using fossil fuels through renewable energy solutions.

I would like one side with specific information (name, address etc)

The other side to be bold, professional company name & logo. Striking.

Target Market(s)

B2B. Transport, mining, councils, environmentalist,

Industry/Entity Type

Petroleum

Contact Information for Business Card

Name; Peter Morrow
Position; Director
Email; pmorrow@korvanse.com.au
Address; PO Box 347, Penrith, NSW, 2751
Website; www.korvanse.com.au

Colors

Designer to choose colors to be used in the design.

Requirements
Must have
• Clean, easy to read, professional & strong theme
Should not have
• too many colours, busy layout,

```html
<!DOCTYPE html>
<html lang="en">
<head>
<meta charset="utf-8">
<title>Korvan Fuel Works – Business Card</title>
<link rel="stylesheet" href="https://fonts.googleapis.com/css2?family=Montserrat:wght@700&family=Questrial&display=swap">
<style>
  :root {
    --navy: #23587c;
    --orange: #f28224;
    --white: #ffffff;
    --ink: #2b2b2b;
    --backdrop: #3a3d42;
  }
  html, body {
    margin: 0;
    padding: 0;
    width: 1200px;
    height: 1000px;
    overflow: hidden;
    background: var(--backdrop);
  }
  .canvas {
    position: relative;
    width: 1200px;
    height: 1000px;
  }
  .card {
    position: absolute;
    left: 250px;
    width: 700px;
    height: 400px;
    border-radius: 22px;
    overflow: hidden;
    box-shadow: 0 12px 30px rgba(0,0,0,0.35);
  }
  .card-back {
    top: 50px;
    background: var(--navy);
    display: flex;
    align-items: center;
    justify-content: center;
  }
  .card-front {
    top: 520px;
    background: var(--white);
  }

  .brand-name {
    margin: 0;
    font-family: "Montserrat", sans-serif;
    font-weight: 700;
    line-height: 1.1;
    letter-spacing: 0.04em;
    text-transform: uppercase;
    white-space: nowrap;
  }
  .card-back .brand-name {
    color: var(--white);
    font-size: 54px;
  }
  .card-front .brand-name {
    position: absolute;
    left: 48px;
    top: 48px;
    color: var(--navy);
    font-size: 30px;
  }

  .contact {
    position: absolute;
    left: 48px;
    top: 140px;
    width: 420px;
  }
  .person-name {
    margin: 0;
    font-family: "Montserrat", sans-serif;
    font-weight: 700;
    font-size: 26px;
    color: var(--navy);
  }
  .person-role {
    margin: 2px 0 0;
    font-family: "Questrial", sans-serif;
    font-size: 18px;
    color: var(--orange);
  }
  .divider {
    height: 2px;
    background: var(--navy);
    margin: 10px 0 12px;
  }
  .details {
    list-style: none;
    margin: 0;
    padding: 0;
    font-family: "Questrial", sans-serif;
    font-size: 17px;
    color: var(--ink);
  }
  .details li {
    display: flex;
    align-items: center;
    gap: 8px;
    height: 28px;
  }
  .details .icon {
    width: 16px;
    height: 16px;
    flex: none;
  }
  .details .no-icon { padding-left: 24px; }

  .sweep {
    position: absolute;
    left: 0;
    top: 0;
    width: 700px;
    height: 400px;
  }
</style>
</head>
<body>
<main class="canvas">

  <section class="card card-back" aria-label="Business card, brand side">
    <p class="brand-name">Korvan Fuel Works</p>
  </section>

  <section class="card card-front" aria-label="Business card, contact side">
    <svg class="sweep" viewBox="0 0 700 400" aria-hidden="true">
      <path d="M0 322 C 160 380, 460 385, 700 205 L700 222 C 470 398, 160 398, 0 342 Z" fill="var(--orange)"/>
      <path d="M150 400 C 390 398, 560 335, 700 238 L700 400 Z" fill="var(--navy)"/>
    </svg>

    <p class="brand-name">Korvan Fuel Works</p>

    <div class="contact">
      <h1 class="person-name">Peter Morrow</h1>
      <p class="person-role">Director</p>
      <div class="divider"></div>
      <ul class="details">
        <li class="no-icon">PO Box 347, Marlow Vale, NSW, 2793</li>
        <li>
          <svg class="icon" viewBox="0 0 16 16" aria-hidden="true">
            <rect x="1" y="3" width="14" height="10" rx="1.5" fill="var(--orange)"/>
            <path d="M2 4.5 L8 9 L14 4.5" fill="none" stroke="var(--white)" stroke-width="1.4"/>
          </svg>
          pmorrow@korvanse.com.au
        </li>
        <li>
          <svg class="icon" viewBox="0 0 16 16" aria-hidden="true">
            <circle cx="8" cy="8" r="7" fill="var(--orange)"/>
            <ellipse cx="8" cy="8" rx="3" ry="7" fill="none" stroke="var(--white)" stroke-width="1.1"/>
            <line x1="1" y1="8" x2="15" y2="8" stroke="var(--white)" stroke-width="1.1"/>
          </svg>
          www.korvanse.com.au
        </li>
      </ul>
    </div>
  </section>

</main>
</body>
</html>
```